Single-sided business card for restaurant bellwether with new logo made on this site

Business card options with new logo including restaurant name, address, phone number and website. This business card is single-sided only and will be presented at the hostess desk for clients to take. I would like to see options based on a cream card background, a white card background, a yellow card background and a burgundy colored background. It needs to be elegant and traditional.

Target Market(s)

local and international crowd

Industry/Entity Type

restaurant

Contact Information for Business Card

address, website and phone number

Font styles to use
Serif

Colors
EE7325
F08F49
F5BC92
FAE3D3
FDF4ED

Requirements
Must have
• new logo, address, phone number, website
Should not have
• more than three colors

```html
<!DOCTYPE html>
<html lang="es">
<head>
<meta charset="utf-8">
<title>Restaurant Bellwether – Business Card Options</title>
<link rel="stylesheet" href="https://fonts.googleapis.com/css2?family=Tinos:wght@400&display=swap">
<style>
  :root {
    --brown: #3d1f1f;
    --gold: #f5b22e;
    --cream: #ffffc8;
    --white: #ffffff;
    --page: #ffffff;
    --band: #000000;
  }
  * { margin: 0; padding: 0; box-sizing: border-box; }
  html, body { width: 1200px; height: 1117px; overflow: hidden; background: var(--page); }
  .sheet { position: relative; width: 1200px; height: 1117px; font-family: "Tinos", "Times New Roman", serif; }

  .card {
    position: absolute; width: 542px; height: 331px;
    background: var(--card-bg); color: var(--card-ink);
  }
  .card--burgundy { left: 33px; top: 137px; --card-bg: var(--brown); --card-ink: var(--white); --plate-bg: var(--gold); --plate-ink: var(--brown); --rule: var(--white); }
  .card--yellow   { left: 625px; top: 137px; --card-bg: var(--gold); --card-ink: var(--brown); --plate-bg: var(--brown); --plate-ink: var(--gold); --rule: var(--brown); }
  .card--white    { left: 33px; top: 493px; --card-bg: var(--white); --card-ink: var(--brown); --plate-bg: var(--brown); --plate-ink: var(--gold); --rule: var(--brown); border: 1px solid #8a8a8a; }
  .card--cream    { left: 625px; top: 493px; --card-bg: var(--cream); --card-ink: var(--brown); --plate-bg: var(--brown); --plate-ink: var(--cream); --rule: var(--brown); }

  .logo-plate {
    position: absolute; left: 46px; top: 76px; width: 124px; height: 180px;
    background: var(--plate-bg);
    display: flex; align-items: center; justify-content: center;
  }
  .logo-plate::before {
    content: ""; position: absolute; inset: 5px;
    border: 2px solid var(--plate-ink);
  }
  .logo-plate__name {
    position: relative;
    font-size: 11px; letter-spacing: 1.2px; line-height: 1;
    white-space: nowrap;
    color: var(--plate-ink);
  }

  .divider { position: absolute; left: 210px; top: 45px; width: 10px; height: 240px; }
  .divider polygon { fill: var(--rule); }

  .details { position: absolute; left: 260px; top: 92px; }
  .details__name { font-size: 34px; font-weight: 400; line-height: 32px; }
  .details__lines { list-style: none; margin-top: 6px; font-size: 14.5px; line-height: 21.6px; }

  .footer-band { position: absolute; left: 0; top: 960px; width: 1200px; height: 157px; background: var(--band); }
</style>
</head>
<body>
<main class="sheet">

  <section class="card card--burgundy">
    <div class="logo-plate"><span class="logo-plate__name">BELLWETHER</span></div>
    <svg class="divider" viewBox="0 0 10 240" aria-hidden="true"><polygon points="5,0 7,120 5,240 3,120"/></svg>
    <div class="details">
      <h2 class="details__name">Restaurant<br>Bellwether</h2>
      <ul class="details__lines">
        <li>Magnolia 415</li>
        <li>Bahías de Costa Clara, Oaxaca CP 70123</li>
        <li>Reservaciones 958-555-0142</li>
        <li>www.bellwether.com.mx</li>
      </ul>
    </div>
  </section>

  <section class="card card--yellow">
    <div class="logo-plate"><span class="logo-plate__name">BELLWETHER</span></div>
    <svg class="divider" viewBox="0 0 10 240" aria-hidden="true"><polygon points="5,0 7,120 5,240 3,120"/></svg>
    <div class="details">
      <h2 class="details__name">Restaurant<br>Bellwether</h2>
      <ul class="details__lines">
        <li>Magnolia 415</li>
        <li>Bahías de Costa Clara, Oaxaca CP 70123</li>
        <li>Reservaciones 958-555-0142</li>
        <li>www.bellwether.com.mx</li>
      </ul>
    </div>
  </section>

  <section class="card card--white">
    <div class="logo-plate"><span class="logo-plate__name">BELLWETHER</span></div>
    <svg class="divider" viewBox="0 0 10 240" aria-hidden="true"><polygon points="5,0 7,120 5,240 3,120"/></svg>
    <div class="details">
      <h2 class="details__name">Restaurant<br>Bellwether</h2>
      <ul class="details__lines">
        <li>Magnolia 415</li>
        <li>Bahías de Costa Clara, Oaxaca CP 70123</li>
        <li>Reservaciones 958-555-0142</li>
        <li>www.bellwether.com.mx</li>
      </ul>
    </div>
  </section>

  <section class="card card--cream">
    <div class="logo-plate"><span class="logo-plate__name">BELLWETHER</span></div>
    <svg class="divider" viewBox="0 0 10 240" aria-hidden="true"><polygon points="5,0 7,120 5,240 3,120"/></svg>
    <div class="details">
      <h2 class="details__name">Restaurant<br>Bellwether</h2>
      <ul class="details__lines">
        <li>Magnolia 415</li>
        <li>Bahías de Costa Clara, Oaxaca CP 70123</li>
        <li>Reservaciones 958-555-0142</li>
        <li>www.bellwether.com.mx</li>
      </ul>
    </div>
  </section>

  <div class="footer-band"></div>
</main>
</body>
</html>
```